Tovrin Mobile Phone colors and content

Looking to have an impact both on messaging and colors for my mobile website
www.quilvantohar.loan
also, i have upload my first draft of the mobile site, including messaging. that is open to the designer. In the end, i want the mobile phone messaging to resonate for someone who wants to build their credit.
Dont worry about the color combination on the document.

Target Market(s)

Finance - those with super poor credit.

Industry/Entity Type

Finance - credit building

Number of Pages Required

5+ page

Font styles to use
Other font styles liked:
• Inter

Requirements
Must have
• flow and impact
Nice to have
• look at the documents uploaded
Should not have
• not have dark background colors. background should be white.

```html
<!DOCTYPE html>
<html lang="en">
<head>
<meta charset="utf-8">
<title>Ravell Credit – Credit Builder Loans</title>
<link rel="stylesheet" href="https://fonts.googleapis.com/css2?family=Inter:wght@400;500;600;700;800&display=swap">
<style>
  :root {
    --ink: #111418;
    --body: #2a2d33;
    --green: #17c24f;
    --green-btn: #12c052;
    --blue: #3a5fe0;
    --page-top: #e6f8ec;
    --page-bottom: #eff1fb;
    --screen-top: #e9f9ef;
    --screen-mid: #ffffff;
    --screen-bottom: #eef0fc;
    --divider: #b7dcc6;
    --placeholder: #cfd9ee;
  }
  * { box-sizing: border-box; margin: 0; padding: 0; }
  html, body { width: 900px; height: 1200px; overflow: hidden; }
  body {
    position: relative;
    font-family: "Inter", sans-serif;
    color: var(--ink);
    background: linear-gradient(180deg, var(--page-top) 0%, #f6fbf8 40%, var(--page-bottom) 100%);
  }

  .brand-header { position: absolute; top: 72px; left: 0; width: 900px; text-align: center; }
  .brand-name { font-size: 33px; font-weight: 800; letter-spacing: -0.5px; color: var(--ink); }
  .brand-tagline { margin-top: 6px; font-size: 20px; font-weight: 700; color: var(--green); }

  .screen {
    position: absolute;
    width: 162px; height: 353px;
    border-radius: 22px;
    border: 1px solid #dfe4ee;
    background: linear-gradient(180deg, var(--screen-top) 0%, var(--screen-mid) 40%, var(--screen-bottom) 100%);
    box-shadow: 0 6px 18px rgba(40, 60, 90, 0.08);
    display: flex; flex-direction: column; align-items: center;
    padding: 26px 5px 0;
    text-align: center;
  }
  .screen-logo { font-size: 8px; font-weight: 800; color: var(--ink); line-height: 1; }
  .screen-logo-sub { margin-top: 3px; font-size: 4.5px; font-weight: 700; color: var(--green); }
  .screen-divider { width: 150px; height: 1px; background: var(--divider); margin-top: 11px; }

  .step-pill {
    margin-top: 12px;
    border: 1px solid var(--blue);
    color: var(--blue);
    border-radius: 8px;
    font-size: 5.5px; font-weight: 600;
    padding: 2px 9px;
  }
  .screen-title { font-size: 9.6px; font-weight: 500; line-height: 1.55; color: var(--ink); white-space: nowrap; }
  .accent { color: var(--green); }
  .screen-lead { font-size: 9px; font-weight: 600; color: var(--blue); margin-top: 18px; }
  .screen-text { font-size: 7.2px; line-height: 1.72; color: var(--body); }
  .screen-text + .screen-text { margin-top: 10px; }

  .apply-button {
    position: absolute; left: 50%; top: 307px;
    transform: translateX(-50%);
    width: 78px; height: 25px; border-radius: 13px;
    background: var(--green-btn); color: #fff;
    font-size: 7.5px; font-weight: 600;
    display: flex; align-items: center; justify-content: center;
  }

  .mascot-area {
    margin-top: 12px; width: 52px; height: 64px; border-radius: 10px;
    background: linear-gradient(180deg, #dbe6f6, var(--placeholder));
  }
  .mascot-name { font-size: 6.5px; color: #2b4a8a; margin-top: 3px; }

  .card-shield-area {
    margin-top: 10px; width: 72px; height: 66px; border-radius: 6px;
    background: linear-gradient(180deg, #dde5f8, #d8efe1);
  }

  .flow-line { position: absolute; left: 0; top: 0; }
</style>
</head>
<body>

<header class="brand-header">
  <div class="brand-name">Ravell Credit</div>
  <div class="brand-tagline">Credit Builder Loans</div>
</header>

<svg class="flow-line" width="900" height="1200" viewBox="0 0 900 1200" aria-hidden="true">
  <g fill="none" stroke="#3a5fe0" stroke-width="1" stroke-dasharray="3 3">
    <path d="M271 418 H343"/>
    <path d="M552 418 H624"/>
    <path d="M731 634 V683 H309 V724"/>
    <path d="M412 933 H484"/>
  </g>
  <g fill="#3a5fe0">
    <circle cx="271" cy="418" r="2.6"/><path d="M342 414 L348 418 L342 422 Z"/>
    <circle cx="552" cy="418" r="2.6"/><path d="M623 414 L629 418 L623 422 Z"/>
    <circle cx="731" cy="634" r="2.6"/><path d="M305 723 L309 729 L313 723 Z"/>
    <circle cx="412" cy="933" r="2.6"/><path d="M483 929 L489 933 L483 937 Z"/>
  </g>
</svg>

<section class="screen" style="left:89px; top:241px;">
  <div class="screen-logo">Ravell Credit</div>
  <div class="screen-logo-sub">Credit Builder Loans</div>
  <div class="screen-divider"></div>
  <h2 class="screen-title" style="margin-top:13px;">A Better Way to<br>Rebuild Credit — <span class="accent">3 Bold Steps</span></h2>
  <p class="screen-lead">Rebuilding your credit?</p>
  <p class="screen-text" style="margin-top:10px; padding:0 6px;">We'll help you do it effectively—with real tools, real progress, and real incentives.</p>
  <div class="apply-button">Apply now</div>
</section>

<section class="screen" style="left:369px; top:241px;">
  <div class="screen-logo">Ravell Credit</div>
  <div class="screen-logo-sub">Credit Builder Loans</div>
  <div class="screen-divider"></div>
  <div class="step-pill">Step 1</div>
  <div class="mascot-area" role="img" aria-label="Illustration of the Dr. Ravell guide character in a lab coat"></div>
  <div class="mascot-name">Dr. Ravell</div>
  <svg width="18" height="26" viewBox="0 0 18 26" style="margin-top:12px;" aria-hidden="true">
    <rect x="1" y="1" width="16" height="24" fill="#fff" stroke="#3a5fe0" stroke-width="1"/>
    <g stroke="#17c24f" stroke-width="1"><path d="M4 7H14M4 10H14M4 13H14M4 16H12"/></g>
    <path d="M4 21 L7 19 L9 22 L13 19" stroke="#3a5fe0" fill="none" stroke-width="0.8"/>
  </svg>
  <h2 class="screen-title" style="margin-top:12px;">A $2,000 <span class="accent">Credit<br>Builder Loan</span></h2>
  <p class="screen-text" style="margin-top:6px;">Make on-time payments on a $2,000 Credit Builder Loan designed to help establish real credit history.</p>
  <div class="apply-button">Apply now</div>
</section>

<section class="screen" style="left:649px; top:241px;">
  <div class="screen-logo">Ravell Credit</div>
  <div class="screen-logo-sub">Credit Builder Loans</div>
  <div class="screen-divider"></div>
  <div class="step-pill">Step 2 – Platinum Rise Status</div>
  <svg width="26" height="24" viewBox="0 0 26 24" style="margin-top:10px;" aria-hidden="true">
    <rect x="1" y="1" width="18" height="14" fill="#fff" stroke="#3a5fe0" stroke-width="1"/>
    <rect x="5" y="5" width="19" height="14" fill="#fff" stroke="#3a5fe0" stroke-width="1"/>
    <path d="M8 10H18M8 13H16" stroke="#17c24f" stroke-width="1"/>
    <circle cx="20" cy="18" r="4.5" fill="#fff" stroke="#17c24f" stroke-width="1"/>
    <path d="M18 18 L19.5 19.5 L22 16.8" fill="none" stroke="#17c24f" stroke-width="1"/>
  </svg>
  <h2 class="screen-title" style="margin-top:12px;"><span class="accent">We Put Our Money</span> Where<br>Our Mouth is</h2>
  <p class="screen-text" style="margin-top:8px;">Upon reaching Platinum Rise Status, eligible members may receive a matching contribution of up to $150 toward an approved secured credit card.</p>
  <p class="screen-text">A strong on-time payment history<br>with us is required.</p>
  <p class="screen-text">Your responsible progress unlocks real value—not gimmicks.</p>
  <div class="apply-button">Apply now</div>
</section>

<section class="screen" style="left:229px; top:757px;">
  <div class="screen-logo">Ravell Credit</div>
  <div class="screen-logo-sub">Credit Builder Loans</div>
  <div class="screen-divider"></div>
  <div class="step-pill">Step 3 – Elite Status</div>
  <div class="card-shield-area" role="img" aria-label="Illustration of a credit card with a protective shield"></div>
  <h2 class="screen-title" style="margin-top:10px;">Graduate to a Larger Credit Line<br>with an <span class="accent">Unsecured Kestrel<br>Creditcard</span></h2>
  <p class="screen-text" style="margin-top:8px;">Continued responsible use may qualify you for a higher-credit-limit unsecured credit card.</p>
  <p class="screen-text">No security deposit would be required.</p>
  <div class="apply-button">Apply now</div>
</section>

<section class="screen" style="left:509px; top:757px;">
  <div class="screen-logo">Ravell Credit</div>
  <div class="screen-logo-sub">Credit Builder Loans</div>
  <div class="screen-divider"></div>
  <h2 class="screen-title" style="margin-top:13px;">Ongoing<br><span class="accent">Credit Wellness</span></h2>
  <p class="screen-text" style="margin-top:9px;">Track your progress, monitor your credit,<br>and get guidance along the way.</p>
  <p class="screen-text">Dr. Ravell helps you understand<br>what matters—and provides concrete strategies to improve your credit.</p>
  <div class="apply-button">Apply now</div>
</section>

</body>
</html>
```